BOLD Gym Needs a New WALL WRAP!

We have a small wall that we need to spice up and we'd like to wrap it with a bold design that stands out and breaks up the current bland grey color.
The wall itself is 128.25" long x 50.5" tall
I am open to design options, but the design must include our PulvaRex logo (attached)
I have also included photos of the gym to give you an idea of the vibe, colors, etc.
DO NOT BE AFRAID OF COLOR😊​ Although our colors are Yellow, Grey's, Blacks, etc., in the gym, please do not be afraid to play with color while still making it look like it belongs in our building. The posters that hang around that wall have pinks, purples, etc. in it. I've included a poster for you to see the colors that are nearby.
The photo from the ground looking up towards the second story highlights the wall that needs to be wrapped.
The ultimate goal here is to break up the grey wall with a killer design.

```html
<!DOCTYPE html>
<html lang="en">
<head>
<meta charset="utf-8">
<title>PulvaRex Wall Wrap</title>
<link rel="stylesheet" href="https://fonts.googleapis.com/css2?family=Montserrat:wght@700;900&display=swap">
<style>
  :root {
    --charcoal: #2a2a2c;
    --gym-yellow: #f6cd16;
    --chalk-white: #ffffff;
    --olive-dot: #6b6225;
  }
  html, body {
    margin: 0;
    padding: 0;
    width: 1200px;
    height: 473px;
    overflow: hidden;
    background: var(--charcoal);
  }
  .wall-wrap {
    display: block;
    width: 1200px;
    height: 473px;
  }
  .side-band--white { fill: var(--chalk-white); }
  .side-band--dark { fill: var(--charcoal); }
  .side-band--yellow { fill: var(--gym-yellow); }
  .center-field { fill: var(--charcoal); }
  .brand-name {
    font-family: "Montserrat", sans-serif;
    font-weight: 900;
    fill: var(--chalk-white);
  }
  .tagline {
    font-family: "Montserrat", sans-serif;
    font-weight: 700;
    fill: var(--gym-yellow);
    letter-spacing: 12px;
  }
  .barbell-icon { fill: var(--chalk-white); }
</style>
</head>
<body>
<svg class="wall-wrap" viewBox="0 0 2576 1016" preserveAspectRatio="none" xmlns="http://www.w3.org/2000/svg">
  <defs>
    <radialGradient id="halftone-glow" cx="50%" cy="50%" r="50%">
      <stop offset="0%" stop-color="#6b6225" stop-opacity="0.9"/>
      <stop offset="60%" stop-color="#4a4526" stop-opacity="0.6"/>
      <stop offset="100%" stop-color="#2a2a2c" stop-opacity="0"/>
    </radialGradient>
    <linearGradient id="fist-down" x1="0" y1="0" x2="0" y2="1">
      <stop offset="0%" stop-color="#f6cd16"/>
      <stop offset="100%" stop-color="#fbf3d0"/>
    </linearGradient>
    <linearGradient id="fist-up" x1="0" y1="1" x2="0" y2="0">
      <stop offset="0%" stop-color="#f6cd16"/>
      <stop offset="100%" stop-color="#fbf3d0"/>
    </linearGradient>
  </defs>

  <!-- center field -->
  <rect class="center-field" x="260" y="0" width="2058" height="1016"/>
  <ellipse cx="1288" cy="500" rx="820" ry="470" fill="url(#halftone-glow)" role="img" aria-label="Halftone dot pattern glowing behind the brand name"/>

  <!-- left stripe panel -->
  <g class="side-panel side-panel--left">
    <rect class="side-band--dark" x="0" y="0" width="260" height="1016"/>
    <polygon class="side-band--white" points="0,0 260,0 260,120 0,335"/>
    <polygon class="side-band--yellow" points="0,470 260,260 260,1016 0,1016"/>
  </g>

  <!-- right stripe panel -->
  <g class="side-panel side-panel--right">
    <rect class="side-band--dark" x="2318" y="0" width="258" height="1016"/>
    <polygon class="side-band--yellow" points="2318,0 2576,0 2576,555 2318,760"/>
    <polygon class="side-band--white" points="2318,890 2576,690 2576,1016 2318,1016"/>
  </g>

  <!-- hanging fists, top row -->
  <g class="fist-row fist-row--top" fill="url(#fist-down)">
    <g role="img" aria-label="Illustrated clenched fist hanging from above">
      <rect x="370" y="0" width="60" height="250"/><rect x="330" y="240" width="145" height="140"/></g>
    <g role="img" aria-label="Illustrated clenched fist hanging from above">
      <rect x="595" y="0" width="60" height="90"/><rect x="555" y="80" width="145" height="140"/></g>
    <g role="img" aria-label="Illustrated clenched fist hanging from above">
      <rect x="815" y="0" width="60" height="30"/><rect x="775" y="20" width="145" height="140"/></g>
    <g role="img" aria-label="Illustrated clenched fist hanging from above">
      <rect x="1035" y="0" width="60" height="125"/><rect x="995" y="115" width="145" height="140"/></g>
    <g role="img" aria-label="Illustrated clenched fist hanging from above">
      <rect x="1260" y="0" width="60" height="55"/><rect x="1218" y="45" width="145" height="140"/></g>
    <g role="img" aria-label="Illustrated clenched fist hanging from above">
      <rect x="1480" y="0" width="60" height="110"/><rect x="1438" y="100" width="145" height="140"/></g>
    <g role="img" aria-label="Illustrated clenched fist hanging from above">
      <rect x="1660" y="0" width="145" height="95"/></g>
    <g role="img" aria-label="Illustrated clenched fist hanging from above">
      <rect x="1925" y="0" width="60" height="80"/><rect x="1882" y="70" width="145" height="140"/></g>
    <g role="img" aria-label="Illustrated clenched fist hanging from above">
      <rect x="2145" y="0" width="60" height="250"/><rect x="2103" y="240" width="145" height="140"/></g>
  </g>

  <!-- raised fists, bottom row -->
  <g class="fist-row fist-row--bottom" fill="url(#fist-up)">
    <g role="img" aria-label="Illustrated raised clenched fist">
      <rect x="330" y="635" width="145" height="140"/><rect x="370" y="765" width="60" height="251"/></g>
    <g role="img" aria-label="Illustrated raised clenched fist">
      <rect x="555" y="800" width="145" height="140"/><rect x="595" y="930" width="60" height="86"/></g>
    <g role="img" aria-label="Illustrated raised clenched fist">
      <rect x="775" y="855" width="145" height="140"/><rect x="815" y="985" width="60" height="31"/></g>
    <g role="img" aria-label="Illustrated raised clenched fist">
      <rect x="995" y="760" width="145" height="140"/><rect x="1035" y="890" width="60" height="126"/></g>
    <g role="img" aria-label="Illustrated raised clenched fist">
      <rect x="1218" y="835" width="145" height="140"/><rect x="1260" y="965" width="60" height="51"/></g>
    <g role="img" aria-label="Illustrated raised clenched fist">
      <rect x="1438" y="775" width="145" height="140"/><rect x="1480" y="905" width="60" height="111"/></g>
    <g role="img" aria-label="Illustrated raised clenched fist">
      <rect x="1660" y="895" width="145" height="121"/></g>
    <g role="img" aria-label="Illustrated raised clenched fist">
      <rect x="1882" y="800" width="145" height="140"/><rect x="1925" y="930" width="60" height="86"/></g>
    <g role="img" aria-label="Illustrated raised clenched fist">
      <rect x="2103" y="635" width="145" height="140"/><rect x="2145" y="765" width="60" height="251"/></g>
  </g>

  <!-- brand name -->
  <text class="brand-name" x="1288" y="615" text-anchor="middle" font-size="340" textLength="1370" lengthAdjust="spacingAndGlyphs">PulvaRex</text>

  <!-- tagline with barbell icons -->
  <g class="barbell-icon">
    <rect x="757" y="668" width="8" height="44"/>
    <rect x="770" y="660" width="12" height="60"/>
    <rect x="787" y="660" width="12" height="60"/>
    <rect x="804" y="672" width="8" height="36"/>
    <rect x="1772" y="660" width="12" height="60"/>
    <rect x="1789" y="660" width="12" height="60"/>
    <rect x="1806" y="668" width="8" height="44"/>
  </g>
  <text class="tagline" x="1288" y="708" text-anchor="middle" font-size="52" textLength="905" lengthAdjust="spacing">PERSONAL GROUP TRAINING</text>
</svg>
</body>
</html>
```